Ridgeway Moss - Facebook Cover Photo & Photo Icon Design

We’re looking for a Facebook Cover Photo and Profile Icon design for Ridgeway Moss, a leading Residential Real Estate brand under Ridgeway Property Agents, based in Capalaba and Alexandra Hills, Queensland, Australia.

This design will represent my professional real estate profile and needs to be bold, clean, and on-brand.

Deliverables:

Facebook Cover Photo (820 x 312 px, optimized for mobile + desktop)

Facebook Profile Icon (1:1 ratio, minimum 320 x 320 px)

Design Guidelines:

1. Must Include:

The Ridgeway Moss logo (provided after project start)

Use of the Ridgeway Property Agents brand colour palette (will be supplied)

Clear connection to residential real estate

2. Optional but Preferred:

A local photo or skyline of Capalaba or Alexandra Hills in QLD (bonus points for this)

Space for a short tagline like:
“Pricing Sharper. Moving Quicker. Living Ridgeway.”
(Optional tagline – open to variations if it improves layout/design)

3. Style & Feel:

Professional yet personable

Clean, modern aesthetic

Subtle touches of fun or personality are welcome

Layout must work well when overlaid by Facebook UI elements (like profile photo & call-to-action buttons)

Who I Am:
I'm a well-known residential real estate agent in the Redlands area, known for high-energy campaigns, premium video marketing, and a results-driven approach. My brand is fun, fresh, and high-performing — just like the real estate campaigns I run.

Files to be Provided (after selection):

Ridgeway Moss logo in high-res

Brand colour palette / style reference

Optional photo references if local imagery is not sourced by designer

Final Notes:

Make sure all text is legible on mobile and desktop

Original, layered design files must be delivered (PSD or AI preferred)

Bonus points if it feels uniquely “Bayside Queensland” while maintaining a national-level professional polish

Target Market(s)

Hollowmere, Carrick Vale & Ashdown

Industry/Entity Type

Real Estate

Colors
0054AA
0677BA
7BADD7
CADEEF
E8F1F8

Requirements
Must have
• Headshot, Mobile Number 0491 726 805, Suburbs - Hollowmere, Carrick Vale & Ashdown
Nice to have
• White, Crisp & Professional. Bottom Banner with Suburb List. Specialising in Hollowmere, Carrick Vale & Ashdown

```html
<!DOCTYPE html>
<html lang="en">
<head>
<meta charset="utf-8">
<title>Ridgeway Moss – Cover & Profile Icon</title>
<link rel="stylesheet" href="https://fonts.googleapis.com/css2?family=Jost:wght@400&family=Cabin+Condensed:wght@500;600&display=swap">
<style>
  :root {
    --page-bg: #e9ebee;
    --navy: #0b1568;
    --navy-glow: #1a2a8c;
    --plum: #3e2f5e;
    --gold: #f5b25c;
    --white: #ffffff;
    --photo-warm: #6b7a92;
    --photo-dark: #2c3650;
    --sky-top: #3f7fd0;
    --sky-mid: #9cc4e8;
    --water: #7d8c8f;
  }
  * { margin: 0; padding: 0; box-sizing: border-box; }
  html, body { width: 1200px; height: 786px; overflow: hidden; background: var(--page-bg); }
  body { position: relative; font-family: "Cabin Condensed", sans-serif; }

  .cover {
    position: absolute; left: 40px; top: 40px;
    width: 1120px; height: 421px; overflow: hidden;
  }
  .cover-art { position: absolute; inset: 0; display: block; }

  .brand-mark {
    position: absolute; left: 560px; top: 56px; transform: translateX(-50%);
    text-align: center; color: var(--white);
    font-family: "Jost", sans-serif; font-weight: 400; line-height: 1;
  }
  .brand-mark .brand-first { display: block; font-size: 36px; letter-spacing: 5px; }
  .brand-mark .brand-last { display: block; font-size: 84px; letter-spacing: 6px; margin-top: 0; }

  .tagline {
    position: absolute; left: 560px; top: 194px; transform: translateX(-50%);
    white-space: nowrap; color: var(--gold); font-size: 23px; font-weight: 500;
  }
  .suburbs {
    position: absolute; left: 560px; top: 240px; transform: translateX(-50%);
    white-space: nowrap; text-align: center; color: var(--gold);
    font-size: 26px; font-weight: 500; line-height: 31px;
  }
  .phone {
    position: absolute; left: 560px; top: 334px; transform: translateX(-50%);
    display: flex; align-items: center; gap: 10px;
    color: var(--gold); font-size: 32px; font-weight: 600; white-space: nowrap;
  }
  .phone svg { width: 30px; height: 30px; display: block; }

  .profile-icon {
    position: absolute; left: 470px; top: 500px;
    width: 260px; height: 260px; border-radius: 50%;
    background: var(--navy); border: 6px solid var(--white);
    box-shadow: 0 0 0 2px #c9ced8;
    display: flex; flex-direction: column; align-items: center; justify-content: center;
    color: var(--white); font-family: "Jost", sans-serif; font-weight: 400; line-height: 1;
  }
  .profile-icon .brand-first { font-size: 24px; letter-spacing: 4px; }
  .profile-icon .brand-last { font-size: 52px; letter-spacing: 4px; margin-top: 2px; }
</style>
</head>
<body>

<section class="cover">
  <svg class="cover-art" viewBox="0 0 1120 421" xmlns="http://www.w3.org/2000/svg">
    <defs>
      <radialGradient id="navyField" cx="0.5" cy="0.5" r="0.6">
        <stop offset="0" stop-color="var(--navy-glow)"/>
        <stop offset="1" stop-color="var(--navy)"/>
      </radialGradient>
      <linearGradient id="headshotTone" x1="0" y1="0" x2="0" y2="1">
        <stop offset="0" stop-color="var(--photo-warm)"/>
        <stop offset="1" stop-color="var(--photo-dark)"/>
      </linearGradient>
      <linearGradient id="skylineTone" x1="0" y1="0" x2="0" y2="1">
        <stop offset="0" stop-color="var(--sky-top)"/>
        <stop offset="0.6" stop-color="var(--sky-mid)"/>
        <stop offset="1" stop-color="var(--water)"/>
      </linearGradient>
    </defs>

    <rect class="navy-field" width="1120" height="408" fill="url(#navyField)"/>
    <polygon class="accent-stripe" points="10,0 230,0 400,408 180,408" fill="var(--plum)" opacity="0.85"/>
    <polygon class="accent-stripe-dark" points="0,0 10,0 180,408 0,408" fill="var(--navy)" opacity="0.6"/>

    <path class="headshot" role="img" aria-label="Headshot of the agent in a blue blazer and white shirt"
          d="M45 408 L60 250 Q70 200 130 180 L160 40 Q170 18 215 18 Q260 18 270 40 L290 180 Q345 200 352 250 L362 408 Z"
          fill="url(#headshotTone)"/>

    <polygon class="skyline" role="img" aria-label="Photo of a riverside city skyline with boats on the water"
             points="685,0 1120,0 1120,408 880,408" fill="url(#skylineTone)"/>
    <polygon class="gold-slash" points="720,92 734,92 834,282 820,282" fill="var(--gold)"/>

    <rect class="bottom-band" y="408" width="1120" height="13" fill="var(--gold)"/>
  </svg>

  <div class="brand-mark">
    <span class="brand-first">RIDGEWAY</span>
    <span class="brand-last">MOSS</span>
  </div>

  <p class="tagline">Pricing Sharper. Moving Quicker. Living Ridgeway.</p>

  <p class="suburbs">- Suburbs -<br>Hollowmere, Carrick Vale &amp; Ashdown</p>

  <p class="phone">
    <svg viewBox="0 0 28 28" aria-hidden="true">
      <circle cx="14" cy="14" r="14" fill="var(--gold)"/>
      <path d="M9.5 7.5 L12 7 L13.5 10.5 L12 12 Q13.2 14.8 16 16 L17.5 14.5 L21 16 L20.5 18.5 Q19.5 20.5 17 20 Q10 18 8 11 Q7.5 8.5 9.5 7.5 Z" fill="var(--navy)"/>
    </svg>
    0491 726 805
  </p>
</section>

<div class="profile-icon">
  <span class="brand-first">RIDGEWAY</span>
  <span class="brand-last">MOSS</span>
</div>

</body>
</html>
```